CD Cover for collection of relaxation music called "Under Quiet Willows"

We'd like to design a CD cover for upload to Brellan Press on Request and to digital services like Tunvo. The template and size specs, photos, example font and text are attached. We need the song durations on the back cover as well and we expect to have those ready by Thursday. Other album and book covers are provided for use as thumbnails inside booklet next to titles. In addition to the finished images to the template specifications, we'd like a copy of the front cover and the back cover as square images to upload to digital services - 2500 dpi x 2500 dpi or larger in .png and .jpg formats. We will also need to add "For more information, visit CalmSoundHarbor.example" under the other available works list. Thanks and we look forward to working together.

Target Market(s)

Relaxation and meditation music. Yoga studios. Massage therapists. Reiki practitioners.

Industry/Entity Type

Music Download

Colors

Designer to choose colors to be used in the design.

Requirements
Must have
• Font consistent with previous works and a peaceful and attractive layout. Also, designers have discretion on which water images to use in which location. The goal is to have a cover image that stands out among other thumbnails in the stores and also for the images on the CD to tell a story of increasing peace and relaxation.

```html
<!DOCTYPE html>
<html lang="en">
<head>
<meta charset="utf-8">
<title>Under Quiet Willows — Album Cover</title>
<link href="https://fonts.googleapis.com/css2?family=Tangerine:wght@400;700&display=swap" rel="stylesheet">
<style>
  :root {
    --sky-top: #b9cde0;
    --sky-mid: #a79cbd;
    --sky-lilac: #b79ab8;
    --horizon-glow: #e89a96;
    --horizon-peach: #f0b29a;
    --treeline: #1f2a2a;
    --water-glow: #c98f9e;
    --water-mid: #8e86a2;
    --water-deep: #5c6479;
    --water-base: #46506a;
    --type: #ffffff;
    --type-shadow: rgba(60, 50, 90, 0.55);
  }
  * { margin: 0; padding: 0; box-sizing: border-box; }
  html, body {
    width: 1200px;
    height: 1177px;
    overflow: hidden;
    background: var(--water-base);
  }
  .album-cover {
    position: relative;
    width: 1200px;
    height: 1177px;
    overflow: hidden;
    font-family: "Tangerine", cursive;
    color: var(--type);
  }
  .cover-scene {
    position: absolute;
    inset: 0;
    background: linear-gradient(
      to bottom,
      var(--sky-top) 0%,
      var(--sky-mid) 22%,
      var(--sky-lilac) 33%,
      var(--horizon-glow) 40%,
      var(--horizon-peach) 44%,
      var(--horizon-glow) 47%,
      var(--treeline) 49%,
      var(--treeline) 53%,
      var(--water-glow) 57%,
      var(--water-mid) 70%,
      var(--water-deep) 86%,
      var(--water-base) 100%
    );
  }
  .cover-text {
    position: absolute;
    left: 0;
    width: 100%;
    text-align: center;
    font-weight: 700;
    line-height: 1;
    text-shadow: 0 0 14px var(--type-shadow), 0 2px 4px var(--type-shadow);
    white-space: nowrap;
  }
  .album-title {
    top: 62px;
    font-size: 176px;
    letter-spacing: 1px;
  }
  .album-subtitle {
    top: 262px;
    font-size: 118px;
    line-height: 142px;
  }
  .artist-name {
    top: 948px;
    font-size: 112px;
  }
</style>
</head>
<body>
  <main class="album-cover">
    <div class="cover-scene" role="img" aria-label="Photograph of a calm lake at sunset: lilac and pink sky above a dark treeline, mirrored in still water"></div>
    <h1 class="cover-text album-title">Under Quiet Willows</h1>
    <p class="cover-text album-subtitle">Healing Music for<br>Body, Mind and Spirit</p>
    <p class="cover-text artist-name">Clara Hollis-Merrow</p>
  </main>
</body>
</html>
```